Kovrix - consultancy website

I need a new design for my webpage/presence [to be functioning with Wordpress - I have a programmer to set it up but not the design idea].
My company is Kovrix - a consultancy firm focused on growth management for Swedish SME's primarily;. We call it Leadership add-on for firms on the rise, kind of a doctor helping small become big. Contentwise, its a simple frontpage + 3-4 subpages with content re company/myself/focus etc. The new site should communicate a fresh, trustworthy take yet simple and functional on all devices [i.e. think UI compatible for mobile/tablet]. Current building parts/form elements are
a) existing logo and text elements
b) existing pictures
c) the yellowish color
colours and new ideas on pictures/positioning are welcome. I prefer a 'full width page' solution with centralised text elements but that's all up to you to suggest. Current site is a quickfix made by myself - now I'm moving it to a new platform so want to take the opportunity to make it
Nothing superspecial as it is a 2-man show; on the other hand I still want to have a modern & fresh reflection of my brand in digital environments. Help me out!
www.kovrix-demo.se
Best
Lotta Bergqvalm

```html
<!DOCTYPE html>
<html lang="en">
<head>
<meta charset="utf-8">
<title>Kovrix – Gallery</title>
<link href="https://fonts.googleapis.com/css2?family=Arimo:wght@400;700&family=Noto+Serif:wght@400&display=swap" rel="stylesheet">
<style>
:root{
  --accent:#e0962a;
  --ink:#222;
  --muted:#666;
  --band:#2b2b2b;
  --cta:#333333;
  --footer:#1b1b1b;
  --footer-base:#121212;
  --white:#fff;
  --blue-a:#3b5998;
  --blue-b:#3fa9e0;
  --red-a:#dd4b39;
}
*{margin:0;padding:0;box-sizing:border-box}
html,body{width:819px;height:1200px;overflow:hidden;background:var(--white)}
body{position:relative;font-family:"Arimo",Arial,sans-serif;color:var(--ink)}
.abs{position:absolute}
.site-header{position:absolute;left:0;top:0;width:819px;height:91px;background:var(--white)}
.brand-name{left:67px;top:16px;font-family:"Noto Serif",Georgia,serif;font-size:33px;line-height:1;color:var(--ink)}
.brand-tag{left:69px;top:55px;font-family:"Noto Serif",Georgia,serif;font-size:10.2px;color:var(--ink)}
.main-nav a{position:absolute;top:41px;font-size:10px;color:var(--ink);text-decoration:none}
.main-nav a.is-active{color:var(--accent)}
.nav-underline{left:626px;top:59px;width:73px;height:1px;background:var(--accent)}
.breadcrumb{left:0;top:91px;width:819px;height:35px;background:var(--band);font-size:10px;color:var(--white);padding:13px 0 0 67px}
.breadcrumb span{color:var(--accent);font-weight:700}
.section-title{left:0;top:171px;width:819px;text-align:center;font-size:18px;font-weight:700}
.section-intro{left:64px;top:209px;width:691px;text-align:center;font-size:9.4px;line-height:14.2px;color:var(--muted)}
.filters{top:290px;font-size:9.6px;color:var(--ink)}
.filters.is-active{color:var(--accent)}
.filter-line{left:312px;top:305px;width:36px;height:1px;background:var(--accent)}
.gallery-tile{position:absolute;width:273px;height:192px}
.tile-overlay{background:rgba(224,160,70,.82);color:var(--white);text-align:center;padding:64px 28px 0}
.tile-overlay h3{font-weight:400;font-size:17px;margin-bottom:8px}
.tile-overlay p{font-size:9.2px;line-height:14px}
.cta-band{left:0;top:818px;width:819px;height:191px;background:var(--cta);text-align:center;color:var(--white)}
.cta-band h2{position:absolute;left:0;top:51px;width:819px;font-size:21px;letter-spacing:3px;font-weight:700}
.cta-band p{position:absolute;left:0;top:81px;width:819px;font-size:9px;letter-spacing:1.6px;font-weight:700}
.cta-button{position:absolute;left:355px;top:112px;width:110px;height:29px;border:1.5px solid var(--white);border-radius:3px;font-size:9.6px;font-weight:700;line-height:26px}
.site-footer{left:0;top:1009px;width:819px;height:156px;background:var(--footer);color:var(--white)}
.footer-heading{top:30px;font-size:10px}
.footer-divider{top:29px;width:1px;height:106px;background:#3a3a3a}
.social-box{position:absolute;top:59px;width:49px;height:63px;text-align:center;font-size:8.5px;padding-top:46px}
.social-box i{position:absolute;left:14px;top:9px;width:21px;height:21px;border-radius:50%;background:rgba(255,255,255,.18)}
.footer-note{font-size:7.4px;color:#9a9a9a;line-height:13px}
.email-field{left:365px;top:89px;width:138px;height:19px;background:var(--white);font-size:6.8px;color:#999;padding:6px 0 0 12px}
.email-submit{left:503px;top:89px;width:21px;height:19px;background:var(--accent)}
.footer-menu{left:664px;top:58px;list-style:none;font-size:7.6px;line-height:14.6px}
.base-bar{left:0;top:1165px;width:819px;height:35px;background:var(--footer-base);text-align:center;font-size:7.4px;color:#777;padding-top:14px}
</style>
</head>
<body>
<header class="site-header">
  <div class="abs brand-name">Kovrix.</div>
  <div class="abs brand-tag">Leadership add-on for firms on the rise</div>
  <nav class="main-nav">
    <a style="left:419px">Home</a>
    <a style="left:489px">About Us</a>
    <a style="left:566px">Services</a>
    <a class="is-active" style="left:647px">Gallery</a>
    <a style="left:713px">Contact Us</a>
  </nav>
  <div class="abs nav-underline"></div>
</header>

<div class="abs breadcrumb">Home &nbsp;&gt;&gt;&nbsp; <span>Gallery</span></div>

<h1 class="abs section-title">Our Gallery</h1>
<p class="abs section-intro">Donec eu viverra odio, eu cursus orci. Vestibulum id imperdiet est, non dictum leo. Aenean dictum nunc ex, quis vehicula dolor posuere id. Donec luctus luctus nisl, id porta turpis. Class aptent taciti sociosqu ad litora torquent per conubia nostra, per inceptos himenaeos. Curabitur metus libero, suscipit pretium erat sed, cursus fau­cibus erat. Vestibulum ante ipsum primis in</p>

<div class="abs filters is-active" style="left:326px">All</div>
<div class="abs filters is-active" style="left:357px">|</div>
<div class="abs filters" style="left:383px">Pictures</div>
<div class="abs filters" style="left:438px">|</div>
<div class="abs filters" style="left:464px">Videos</div>
<div class="abs filter-line"></div>

<section>
  <div class="gallery-tile" style="left:0;top:334px;background:linear-gradient(135deg,#f4f4f4,#d9d9dc)" role="img" aria-label="Two business people in grey suits standing back to back"></div>
  <div class="gallery-tile" style="left:273px;top:334px;background:linear-gradient(135deg,#d8c29a,#b99a6a)" role="img" aria-label="Smiling businesswoman in an office"></div>
  <div class="gallery-tile tile-overlay" style="left:273px;top:334px">
    <h3>Lorem ipsum</h3>
    <p>Lorem ipsum dolor sit amet, consectetur adipiscing elit. Fusce finibus vulputate justo sed commodo. Donec in ipsum vitae nulla</p>
  </div>
  <div class="gallery-tile" style="left:546px;top:334px;width:273px;background:linear-gradient(135deg,#4d6f8e,#20364d)" role="img" aria-label="Hand touching a tablet showing charts"></div>
  <div class="gallery-tile" style="left:0;top:526px;background:linear-gradient(135deg,#e6ecef,#aebcc6)" role="img" aria-label="Two colleagues walking through a bright office corridor"></div>
  <div class="gallery-tile" style="left:273px;top:526px;background:linear-gradient(135deg,#8a8d92,#3b3e44)" role="img" aria-label="Handshake over a desk with laptop and reports"></div>
  <div class="gallery-tile" style="left:546px;top:526px;background:linear-gradient(135deg,#fafafa,#e4e4e4)" role="img" aria-label="Stacks of blank business cards"></div>
</section>

<section class="abs cta-band">
  <h2>DONEC EU VIVERRA ODIO, EU CURSUS ORCI.</h2>
  <p>IN VARIUS VENENATIS ELIT, A PLACERAT LACUS. MAURIS SUSCIPIT</p>
  <div class="cta-button">CONTACT NOW</div>
</section>

<footer class="abs site-footer">
  <div class="abs footer-heading" style="left:67px">Let's Connect</div>
  <div class="social-box" style="left:67px;background:var(--blue-a)"><i></i>2598</div>
  <div class="social-box" style="left:122px;background:var(--blue-b)"><i></i>4576</div>
  <div class="social-box" style="left:176px;background:var(--red-a)"><i></i>1269</div>
  <div class="abs footer-divider" style="left:299px"></div>

  <div class="abs footer-heading" style="left:365px">Mailing List</div>
  <p class="abs footer-note" style="left:365px;top:62px">Sign up for our mailing list to get latest<br>updates and offers.</p>
  <div class="abs email-field">Email address</div>
  <svg class="abs email-submit" viewBox="0 0 21 19"><path d="M7 10l2.6 2.6L14.5 7" fill="none" stroke="#fff" stroke-width="1.8"/></svg>
  <p class="abs footer-note" style="left:365px;top:116px;color:#6f6f6f">We respect your privacy</p>
  <div class="abs footer-divider" style="left:597px"></div>

  <div class="abs footer-heading" style="left:664px">Menu</div>
  <ul class="abs footer-menu">
    <li>Home</li><li>About Us</li><li>Services</li><li>Gallery</li><li>Contact Us</li>
  </ul>
</footer>

<div class="abs base-bar">© Copyrights 2015 All Rights Reserved</div>
</body>
</html>
```